Business card for a new innovative and professional lawn care business

We need a business card design for a new lawn care business in Halifax NS Canada. We offer lawn services in Halifax & Bedford. Our services offered include lawn care, garden services, and property maintenance. We take pride in our work and are experienced at what we do. I would like to see a design that is double sided. On the backside I would like the something simple (maybe my logo preferably on blackround (linked below) with website link, Facebook page or something). The front I want to include contact info:
Darren Maple
phone 902-555-0148
email - darrensyardworks.ca
facebook - Friendpage.com/darrensyardworks
Instagram maybe ? - pixgrid.com/darrenyardworks
Serving Halifax and Bedford for 5 years?
I don't want it to have too much information as I will be passing them out in aim to visit website, or call !
We do want it to include lawn care, garden services and property maintenance.
Basic, catchy, and modern looking !
Logo attached below !

Target Market(s)

Passing business cards to everyone I meet or interact with.

Industry/Entity Type

Lawn Care

Contact Information for Business Card

Double sided with some basic information, with catchy colours and easy to look at.

Font styles to use
Sans Serif

Requirements
Must have
• Must be double sided and have :
• Name, Phone, Email, FB, Website, and 3 main services offered - lawn care, property maintenance, garden services
Nice to have
• Would be nice to have instagram link if it goes well on there
Should not have
• Don't want too much writing or images that are distracting

```html
<!DOCTYPE html>
<html lang="en">
<head>
<meta charset="utf-8">
<title>Darren's Yard Works – Business Card</title>
<link rel="stylesheet" href="https://fonts.googleapis.com/css2?family=Open+Sans:wght@400;600;700&display=swap">
<style>
  :root {
    --bg: #ececec;
    --card-black: #0b0b0b;
    --card-white: #ffffff;
    --lime: #7cc242;
    --forest: #0f7a3c;
    --ink: #1a1a1a;
    --ink-soft: #333333;
    --on-dark: #f2f2f2;
  }
  * { box-sizing: border-box; margin: 0; padding: 0; }
  html, body { width: 1200px; height: 900px; overflow: hidden; }
  body {
    background: var(--bg);
    font-family: "Open Sans", Arial, sans-serif;
    position: relative;
  }
  .card {
    position: absolute;
    left: 250px;
    width: 700px;
    height: 400px;
    overflow: hidden;
    box-shadow: 0 6px 18px rgba(0,0,0,0.18);
  }

  /* Back side */
  .card--back { top: 40px; background: var(--card-black); }
  .card--back .brand {
    position: absolute;
    left: 70px; top: 90px;
    display: flex; align-items: center; gap: 14px;
  }
  .brand-dot {
    flex: none;
    width: 22px; height: 22px; border-radius: 50%;
    background: var(--lime);
  }
  .brand-name {
    font-weight: 700; font-size: 46px; color: var(--lime);
    letter-spacing: 0.5px; white-space: nowrap;
  }
  .services {
    position: absolute; left: 70px; top: 230px;
    list-style: none;
    display: flex; gap: 34px;
    color: var(--on-dark); font-size: 17px;
  }
  .services li { display: flex; align-items: center; gap: 8px; white-space: nowrap; }
  .services li::before {
    content: ""; width: 7px; height: 7px; border-radius: 50%;
    background: var(--lime);
  }
  .web-pill {
    position: absolute; left: 70px; top: 290px;
    background: var(--forest); color: var(--on-dark);
    font-size: 18px; padding: 8px 26px; border-radius: 6px;
  }

  /* Front side */
  .card--front { top: 460px; background: var(--card-white); }
  .edge-dark {
    position: absolute; left: 0; top: 190px; width: 22px; height: 210px;
    background: var(--card-black);
  }
  .edge-green {
    position: absolute; left: 22px; top: 190px; width: 28px; height: 210px;
    background: var(--forest);
  }
  .edge-bottom {
    position: absolute; left: 0; bottom: 0; width: 100%; height: 14px;
    background: var(--card-black);
  }
  .edge-bottom-green {
    position: absolute; left: 50px; bottom: 0; width: 270px; height: 14px;
    background: var(--forest);
  }
  .card--front .brand {
    position: absolute; left: 190px; top: 48px;
    display: flex; align-items: center; gap: 14px;
  }
  .brand-name--front { color: var(--forest); font-size: 42px; }
  .person { position: absolute; left: 80px; top: 140px; }
  .person-name { font-weight: 700; font-size: 22px; color: var(--ink); line-height: 28px; }
  .person-role { font-size: 18px; color: var(--ink-soft); line-height: 24px; }
  .contact {
    position: absolute; left: 80px; top: 222px;
    list-style: none; color: var(--ink); font-size: 19px; line-height: 31px;
  }
  .contact li { display: flex; align-items: center; gap: 12px; white-space: nowrap; }
  .contact-icon {
    width: 18px; display: inline-flex; justify-content: center;
    font-weight: 700; font-size: 18px;
  }
  .contact-square {
    width: 12px; height: 12px; background: var(--ink); display: inline-block;
  }
</style>
</head>
<body>

<section class="card card--back" aria-label="Card back">
  <div class="brand">
    <span class="brand-dot"></span>
    <span class="brand-name">Darren's Yard Works</span>
  </div>
  <ul class="services">
    <li>Lawn care</li>
    <li>Property maintenance</li>
    <li>Garden services</li>
  </ul>
  <div class="web-pill">www.darrensyardworks.com</div>
</section>

<section class="card card--front" aria-label="Card front">
  <div class="edge-dark"></div>
  <div class="edge-green"></div>
  <div class="edge-bottom"></div>
  <div class="edge-bottom-green"></div>

  <div class="brand">
    <span class="brand-dot"></span>
    <span class="brand-name brand-name--front">Darren's Yard Works</span>
  </div>

  <div class="person">
    <p class="person-name">Darren Maple</p>
    <p class="person-role">Manager</p>
  </div>

  <ul class="contact">
    <li>
      <span class="contact-icon">
        <svg width="14" height="16" viewBox="0 0 14 16" aria-hidden="true">
          <path d="M3 1 L5.5 1 L6.5 4.5 L4.8 5.8 Q6 9.5 8.6 11.2 L10 9.6 L13 10.8 L13 13.5 Q12 15 10 15 Q2 12 1.2 3.5 Q1.5 1.3 3 1 Z" fill="#1a1a1a"/>
        </svg>
      </span>902-555-0148
    </li>
    <li><span class="contact-icon">@</span>darrensyardworks.ca</li>
    <li><span class="contact-icon"><span class="contact-square"></span></span>Friendpage.com/darrensyardworks</li>
    <li><span class="contact-icon"><span class="contact-square"></span></span>pixgrid.com/darrenyardworks</li>
  </ul>
</section>

</body>
</html>
```